established lighting store -latest lighting designs

I would like a design for a 2 sided brochure (front and back) A4
I own a lighting store and have been servicing and supplying lights for 16 years
We supply lighting to over 100 builders
We work with designers ,architects, home renovators
We have the latest designs and trends in lighting
We offer personalised service to all our customers
We can help you with the lighting design of your new home or commercial project

We currently supply lights to about 20 builders who have display homes in a display village nearby http://nestrova.com.au
These display homes have potential buyers of the homes walking through them and therefore potential customers of ours.
Usually the builder will refer the client to us but it would be nice to have some kind of presence in the display home in the way of a brochure.
This will enable us to possibly pick up client who are just browsing thru the homes

I'd the photos to do most of the talking with a description similar to the brochure attached .(which says "at velia lighting dorrington vale we excel......) PLEASE NOTE COMPANY NAME IS NOW
VELIA LIGHTING MARSH KNOLL

we will need
company name VELIA LIGHTING MARSH KNOLL
logo ATTACHED
address UNIT 27 / 4 PELLAM ST , MARSH KNOLL
phone no 95817430

and an invitation to come into our showroom with their plans to help them with their lighting layout and to help them select the right lighting for their home

i like the idea of black background with the photos overlaping with border around each
photos can be cropped to suit

some sample black background brochures attached

Target Market(s)

NEW HOME OWNERS BUILDING NEW HOMES NEEding lights
builders clients
renovators

Industry/Entity Type

Store

Font styles to use
Sans Serif

Colors
000000
5c5c5c
606060
fbed22
ec1f27
0255a3
00a990
9bcb3c
f37122

Requirements
Must have
• black background
• pictures to be the main focus
• short write up on our services and invitation to visit our store
Nice to have
• please note we are not
• velia lighting dorrington vale (as per some of the previous ads)
• we are now
• velia light marsh knoll
• ++++++++++++++++++++++++++++
• from some wording from our competitors websites
• """"""Velia Lighting is the newest and most distinctive destination for lighting in Sydney. We pride ourselves on sourcing both unique and accessible products with a range that will continue to evolve as new designs and options become available.
• Our service is personalised, and we aim to assist your design choices; be it feature lights in Willoughby, functional lights in Annandale, or an entire home lighting solution.
• Offering a fresh approach to interior and exterior designer lighting in Annandale and Willoughby, our display range includes distinct style European imports through to products that are sourced and manufactured locally. It is our intention to bring together a select range of high quality items to meet the discerning customer’s taste and practical requirements.""""""
• """"""""Here at Brindle Lighting, we have been creating light for over 40 years. Our professional staff, including interior designers and electrical engineers can creatively respond to aesthetic and functional issues with a clear focus on client satisfaction. We are a full-service lighting destination, offering expert advice in layout and design as well as comprehensive style guidance. We are authorised lighting partners with some of the world’s most prestigious and exclusive lighting manufacturers, showcased in our ever-evolving showroom."""
• """Responding to local trends as well as emerging European concepts, we offer an abundance of individual and creative possibilities with an extensive range of contemporary and traditional fittings. We specialise in everything from period restorations to cutting-edge modern and with thousands of stock items, inspiration is never far away. We are truly passionate about light. Come and see why we are different. Call or drop in today or take advantage of our appointment service at Australia’s premiere lighting destination.""""

```html
<!DOCTYPE html>
<html lang="en">
<head>
<meta charset="utf-8">
<title>Velia Lighting Flyer</title>
<link rel="stylesheet" href="https://fonts.googleapis.com/css2?family=Anton&family=Arimo:wght@400;700&family=Lato:ital,wght@0,400;1,400&family=Oswald:wght@600&display=swap">
<style>
  :root {
    --red: #ec1f27;
    --yellow: #fbed22;
    --ink: #000000;
    --silver: #d9d9d9;
    --white: #ffffff;
    --page: #e4e4e4;
  }
  * { margin: 0; padding: 0; box-sizing: border-box; }
  html, body { width: 1200px; height: 1200px; overflow: hidden; background: var(--page); }
  .flyer {
    position: absolute; left: 198px; top: 30px;
    width: 884px; height: 1252px;
    transform: scale(0.9105); transform-origin: 0 0;
    overflow: hidden;
    font-family: "Arimo", Arial, sans-serif;
  }
  .flyer-shapes { position: absolute; inset: 0; width: 884px; height: 1252px; }
  .partners { position: absolute; right: 28px; top: 52px; text-align: right; }
  .partners-title { font-family: "Anton", sans-serif; font-weight: 400; color: var(--yellow); font-size: 48px; line-height: 1.1; letter-spacing: 0.5px; margin-right: 8px; }
  .partners-list { list-style: none; margin-top: 2px; }
  .partners-list li { font-family: "Oswald", sans-serif; font-weight: 600; color: var(--white); font-size: 33px; line-height: 43px; }
  .partners-list li::after { content: ""; display: inline-block; width: 13px; height: 13px; border-radius: 50%; background: var(--yellow); margin-left: 12px; vertical-align: middle; position: relative; top: -3px; }
  .opening-hours { position: absolute; right: 42px; top: 298px; text-align: right; font-size: 26px; line-height: 32px; color: var(--ink); }
  .headline { position: absolute; left: 56px; top: 664px; font-family: "Anton", sans-serif; font-weight: 400; font-size: 52px; line-height: 58px; }
  .headline-accent { color: var(--yellow); display: block; }
  .headline-main { color: var(--white); display: block; }
  .about { position: absolute; left: 57px; top: 808px; width: 408px; }
  .about p { font-family: "Lato", sans-serif; font-style: italic; color: var(--white); font-size: 14.6px; line-height: 19.6px; text-align: justify; margin-bottom: 19.6px; }
  .contact { position: absolute; left: 532px; top: 644px; }
  .contact-label { font-family: "Arimo", sans-serif; font-weight: 700; color: var(--red); font-size: 56px; line-height: 62px; }
  .contact-phone { font-family: "Arimo", sans-serif; font-weight: 400; color: var(--ink); font-size: 72px; line-height: 74px; letter-spacing: -1px; }
  .brand { position: absolute; left: 548px; top: 1084px; display: flex; align-items: center; gap: 10px; }
  .brand-dot { width: 14px; height: 14px; border-radius: 50%; background: var(--yellow); }
  .brand-name { font-family: "Lato", sans-serif; color: var(--white); font-size: 18px; letter-spacing: 1px; }
  .website { position: absolute; left: 0; right: 0; top: 1192px; text-align: center; color: var(--white); font-size: 25px; letter-spacing: 6px; }
</style>
</head>
<body>
<main class="flyer">
  <svg class="flyer-shapes" viewBox="0 0 884 1252">
    <defs>
      <linearGradient id="darkBg" x1="0" y1="0" x2="0" y2="1">
        <stop offset="0" stop-color="#2e2f37"/><stop offset="1" stop-color="#18191d"/>
      </linearGradient>
      <linearGradient id="redFill" x1="0" y1="0" x2="1" y2="1">
        <stop offset="0" stop-color="#ec1f27"/><stop offset="1" stop-color="#d3161f"/>
      </linearGradient>
      <linearGradient id="yellowFill" x1="0" y1="0" x2="1" y2="1">
        <stop offset="0" stop-color="#f9d51a"/><stop offset="0.5" stop-color="#fbed22"/><stop offset="1" stop-color="#f7d61a"/>
      </linearGradient>
      <linearGradient id="silverFill" x1="0" y1="0" x2="1" y2="0">
        <stop offset="0" stop-color="#c9c9c9"/><stop offset="0.5" stop-color="#ffffff"/><stop offset="1" stop-color="#d2d2d2"/>
      </linearGradient>
      <linearGradient id="heroPhoto" x1="0" y1="0" x2="0" y2="1">
        <stop offset="0" stop-color="#3f6fc4"/><stop offset="0.45" stop-color="#7a88a8"/><stop offset="0.75" stop-color="#9a6a3e"/><stop offset="1" stop-color="#1c2440"/>
      </linearGradient>
      <linearGradient id="loungePhoto" x1="0" y1="0" x2="1" y2="1">
        <stop offset="0" stop-color="#b9c8cc"/><stop offset="1" stop-color="#1d86b4"/>
      </linearGradient>
      <linearGradient id="kitchenPhoto" x1="0" y1="0" x2="1" y2="1">
        <stop offset="0" stop-color="#e7e7e7"/><stop offset="0.5" stop-color="#7a5d48"/><stop offset="1" stop-color="#cfcfcf"/>
      </linearGradient>
      <linearGradient id="diningPhoto" x1="0" y1="0" x2="1" y2="1">
        <stop offset="0" stop-color="#8a5a44"/><stop offset="0.5" stop-color="#4d7a3a"/><stop offset="1" stop-color="#6e4a3a"/>
      </linearGradient>
      <linearGradient id="facadePhoto" x1="0" y1="0" x2="1" y2="1">
        <stop offset="0" stop-color="#1d3f95"/><stop offset="0.6" stop-color="#9aa0b8"/><stop offset="1" stop-color="#2a2a30"/>
      </linearGradient>
    </defs>

    <rect class="backdrop" width="884" height="1252" fill="url(#darkBg)"/>
    <rect class="hero-photo" width="884" height="541" fill="url(#heroPhoto)" role="img" aria-label="Photo: modern two-storey home lit at dusk beside a pool"/>

    <polygon class="chevron-white" points="456,0 884,0 884,541 436,541 566,256" fill="#ffffff"/>
    <polygon class="chevron-yellow" points="468,0 884,0 884,541 448,541 578,256" fill="var(--yellow)"/>
    <polygon class="chevron-red" points="484,0 884,0 884,541 464,541 594,256" fill="url(#redFill)"/>
    <polygon class="hours-band" points="582,281 884,281 884,416 521,416" fill="url(#silverFill)"/>

    <rect class="divider" x="0" y="541" width="884" height="15" fill="var(--silver)"/>
    <polygon class="contact-panel" points="494,556 884,556 884,1021 530,1021 494,985" fill="url(#yellowFill)"/>

    <g class="thumbnails">
      <rect x="57" y="461" width="235" height="152" fill="#ffffff"/>
      <rect x="64" y="468" width="221" height="138" fill="url(#loungePhoto)" role="img" aria-label="Photo: poolside lounge with blue cushions"/>
      <rect x="332" y="461" width="235" height="152" fill="#ffffff"/>
      <rect x="339" y="468" width="221" height="138" fill="url(#kitchenPhoto)" role="img" aria-label="Photo: modern kitchen with linear pendant lights"/>
      <rect x="598" y="461" width="235" height="152" fill="#ffffff"/>
      <rect x="605" y="468" width="221" height="138" fill="url(#diningPhoto)" role="img" aria-label="Photo: outdoor dining room with brick columns"/>
    </g>

    <rect x="540" y="801" width="294" height="183" fill="#ffffff"/>
    <rect x="548" y="809" width="278" height="167" fill="url(#facadePhoto)" role="img" aria-label="Photo: lit modern townhouse facade with palm tree at night"/>

    <rect class="footer-rule" x="0" y="1158" width="884" height="14" fill="var(--silver)"/>
    <rect class="footer-band" x="0" y="1172" width="884" height="80" fill="url(#redFill)"/>
  </svg>

  <section class="partners">
    <h2 class="partners-title">We work with</h2>
    <ul class="partners-list">
      <li>Interior Designers</li>
      <li>Architects</li>
      <li>Home renovators</li>
    </ul>
  </section>

  <p class="opening-hours">Monday to Saturday<br>9am till 5pm<br>Sunday 10am till 4pm</p>

  <h1 class="headline">
    <span class="headline-accent">We supply lighting</span>
    <span class="headline-main">to over 100 builders</span>
  </h1>

  <section class="about">
    <p>Velia Lighting has been supplying and servicing lights for 16 years. We pride ourselves on sourcing both unique and accessible products, with the latest designs and trends in lighting for your new home or commercial project.</p>
    <p>Our service is personalised, and we aim to assist your design choices; be it feature lights for your living room, functional lights for your kitchen, or an entire home lighting solution.</p>
    <p>Come and visit our showroom at Unit 27 / 4 Pellam St, Marsh Knoll and bring your house plans with you. Our friendly team will help you with your lighting layout and help you select the right lighting for every room, from European imports through to products made locally.</p>
  </section>

  <section class="contact">
    <h2 class="contact-label">Contact US</h2>
    <p class="contact-phone">95817430</p>
  </section>

  <div class="brand">
    <span class="brand-dot"></span>
    <span class="brand-name">VELIA Lighting</span>
  </div>

  <p class="website">www.velialighting.com.au</p>
</main>
</body>
</html>
```